Business cards and stationary for mobile catering company
Harvest Kettle
Bright & Fun-filled
Martin Probert
Mobile Catering Proprietor
Fernleigh
Corwen Terrace
Ashcombe
Greyshire
KT9 4LP
martin@harvestkettle.co.uk
www.harvestkettle.co.uk
we would like a simple but stylish desing in keeping with our logo
THIS IS OUR LOGO
the . eps file if required

```html
<!DOCTYPE html>
<html lang="en">
<head>
<meta charset="UTF-8">
<title>Harvest Kettle – Business Card</title>
<link href="https://fonts.googleapis.com/css2?family=Lato:wght@400;700&display=swap" rel="stylesheet">
<style>
  :root {
    --page-bg: #ece9e4;
    --card-bg: #ffffff;
    --brand-green: #8dc63f;
    --brand-brown: #4b2a1c;
    --brand-red: #c8302a;
    --text-grey: #5a5a5a;
    --divider: #8dc63f;
  }
  * { box-sizing: border-box; margin: 0; padding: 0; }
  html, body {
    width: 1200px; height: 988px; overflow: hidden;
    background: var(--page-bg);
    font-family: "Lato", sans-serif;
  }
  .canvas {
    width: 1200px; height: 988px;
    display: flex; flex-direction: column;
    align-items: center; justify-content: center; gap: 62px;
  }
  .card {
    width: 700px; height: 400px;
    background: var(--card-bg);
    box-shadow: 0 4px 18px rgba(0,0,0,0.12);
    position: relative;
  }
  .brand {
    display: flex; align-items: center; justify-content: center; gap: 14px;
  }
  .brand-dot {
    width: 34px; height: 34px; border-radius: 50%;
    background: var(--brand-red);
  }
  .brand-name {
    font-weight: 700; color: var(--brand-brown);
    letter-spacing: -0.5px; line-height: 1;
  }
  .card-front .brand { position: absolute; inset: 0; }
  .card-front .brand-name { font-size: 58px; }

  .card-back .brand { position: absolute; top: 58px; left: 0; right: 0; }
  .card-back .brand-dot { width: 26px; height: 26px; }
  .card-back .brand-name { font-size: 46px; }

  .holder {
    position: absolute; top: 148px; left: 0; width: 350px;
    text-align: right; padding-right: 20px;
  }
  .holder-name { font-size: 19px; color: var(--brand-green); font-weight: 700; }
  .holder-role { font-size: 14px; color: var(--text-grey); margin-top: 3px; }

  .details-divider {
    position: absolute; top: 205px; left: 350px;
    width: 2px; height: 120px; background: var(--divider);
  }
  .address {
    position: absolute; top: 214px; left: 0; width: 350px;
    padding-right: 20px; text-align: right;
    font-size: 14px; line-height: 1.55; color: var(--text-grey);
    font-style: normal;
  }
  .contacts {
    position: absolute; top: 214px; left: 352px;
    padding-left: 18px; list-style: none;
    font-size: 14px; color: var(--text-grey);
  }
  .contacts li { display: flex; align-items: center; gap: 10px; height: 32px; }
  .contact-icon { width: 20px; height: 20px; flex: none; }
</style>
</head>
<body>
<main class="canvas">

  <section class="card card-front" aria-label="Card front">
    <div class="brand">
      <span class="brand-dot"></span>
      <span class="brand-name">Harvest Kettle</span>
    </div>
  </section>

  <section class="card card-back" aria-label="Card back">
    <div class="brand">
      <span class="brand-dot"></span>
      <span class="brand-name">Harvest Kettle</span>
    </div>

    <div class="holder">
      <p class="holder-name">Martin Probert</p>
      <p class="holder-role">Mobile Catering Proprietor</p>
    </div>

    <address class="address">
      Fernleigh Corwen Terrace<br>
      Ashcombe Greyshire<br>
      KT9 4LP
    </address>

    <div class="details-divider"></div>

    <ul class="contacts">
      <li>
        <svg class="contact-icon" viewBox="0 0 20 20" aria-hidden="true">
          <circle cx="10" cy="10" r="10" fill="#8dc63f"/>
          <path d="M7 5.5 L8.6 5.5 L9.3 8 L8.2 8.9 Q9.3 11 11.1 11.8 L12 10.7 L14.5 11.4 L14.5 13 Q14.3 14.5 12.8 14.5 Q6 13.8 5.5 7.2 Q5.5 5.7 7 5.5 Z" fill="#fff"/>
        </svg>
        07700 900482
      </li>
      <li>
        <svg class="contact-icon" viewBox="0 0 20 20" aria-hidden="true">
          <circle cx="10" cy="10" r="10" fill="#8dc63f"/>
          <rect x="5" y="6.5" width="10" height="7" fill="none" stroke="#fff" stroke-width="1.3"/>
          <path d="M5 6.5 L10 10.5 L15 6.5" fill="none" stroke="#fff" stroke-width="1.3"/>
        </svg>
        martin@harvestkettle.co.uk
      </li>
      <li>
        <svg class="contact-icon" viewBox="0 0 20 20" aria-hidden="true">
          <circle cx="10" cy="10" r="10" fill="#8dc63f"/>
          <circle cx="10" cy="10" r="5" fill="none" stroke="#fff" stroke-width="1.2"/>
          <ellipse cx="10" cy="10" rx="2.2" ry="5" fill="none" stroke="#fff" stroke-width="1.1"/>
          <line x1="5" y1="10" x2="15" y2="10" stroke="#fff" stroke-width="1.1"/>
        </svg>
        www.harvestkettle.co.uk
      </li>
    </ul>
  </section>

</main>
</body>
</html>
```